Re-style home page - eye-catching and unique design for social commerce website

We need a new concept design for Trondix's home page.
We don't want to make huge changes but creating a more professional and eye-catching style.

We need to look very serious like a professional services company and in the same time to look like a social network for e-commerce.

Our logo is very captive and you can use to creating something of harmonious.

This is a re-style and I'm excepted to see unique and fresh design like Glimmora.
Updates

Target Market(s)

e-commerce and social

Industry/Entity Type

Social

Number of Pages Required

1 page

Font styles to use
Serif
Sans Serif

Requirements
Must have
• An eye-catching result.
• Search bar with logo and Login How it works and business
• The slogan with login and signup.
• Footer links.
Nice to have
• I would like to open the home page and see only two clear ways:
• -Consumer
• --Search
• --The slogan
• --Login and Signup
• --How it works
• -Business
• --Go to Business area
• Background: City, Shopping.
Should not have
• Scrollbar style!

```html
<!DOCTYPE html>
<html lang="en">
<head>
<meta charset="utf-8">
<title>Trondix – Shop directly from your profile</title>
<link href="https://fonts.googleapis.com/css2?family=Open+Sans:wght@400;600&family=Roboto:wght@400;500&family=Roboto+Condensed:wght@400;700&display=swap" rel="stylesheet">
<style>
:root{
  --header-bg:#262626;
  --footer-bg:#1b1b1b;
  --white:#ffffff;
  --nav-text:#e6e6e6;
  --field-border:#dcdcdc;
  --field-text:#555555;
  --signup:#f15a37;
  --login:#e9983b;
  --social-login:#4a6cc0;
  --social-login-dark:#3e5cab;
  --panel-frame:rgba(255,255,255,.55);
  --footer-text:#e8e8e8;
  --icon:#d6d6d6;
}
*{box-sizing:border-box;margin:0;padding:0}
html,body{width:1200px;height:905px;overflow:hidden}
body{font-family:"Open Sans",sans-serif;background:var(--footer-bg);position:relative}
.site-header{position:absolute;left:0;top:0;width:1200px;height:114px;background:var(--header-bg);z-index:2}
.brand{position:absolute;left:99px;top:33px;display:flex;align-items:center;gap:10px;color:var(--white);font-family:"Roboto",sans-serif;font-weight:500;font-size:37px;letter-spacing:-.5px}
.brand-mark{width:22px;height:22px;background:var(--login);border-radius:50%}
.main-nav{position:absolute;top:43px;left:547px;display:flex;gap:29px}
.main-nav a{color:var(--nav-text);text-decoration:none;font-family:"Roboto",sans-serif;font-size:15px;letter-spacing:.8px}
.search{position:absolute;left:843px;top:35px;width:211px;height:33px;background:var(--white);border-radius:3px;display:flex;align-items:center;padding:0 10px 0 15px;justify-content:space-between}
.search span{font-size:12px;color:#333;font-family:"Roboto",sans-serif}
.menu-btn{position:absolute;left:1066px;top:36px;width:36px;height:32px;border:1px solid #ddd;border-radius:4px;display:flex;flex-direction:column;justify-content:center;align-items:center;gap:3px}
.menu-btn i{display:block;width:18px;height:3px;background:#fff;border-radius:1px}
.hero{position:absolute;left:0;top:114px;width:1200px;height:632px;overflow:hidden}
.hero-photo{position:absolute;inset:0;background:
  radial-gradient(ellipse 380px 460px at 930px 300px,#b9855c 0%,#8f6d4f 45%,rgba(120,100,80,0) 75%),
  radial-gradient(ellipse 300px 260px at 560px 470px,rgba(236,126,58,.85),rgba(236,126,58,0) 70%),
  linear-gradient(100deg,#bfa08a 0%,#c9b7a6 35%,#b9a48f 55%,#7d6b59 100%)}
.hero-title{position:absolute;left:0;width:612px;top:70px;text-align:center;color:var(--white);font-family:"Roboto Condensed",sans-serif}
.hero-title h1{font-size:29px;font-weight:400;letter-spacing:-.5px;transform:scaleX(.88)}
.hero-title p{font-size:21px;margin-top:10px;transform:scaleX(.9)}
.slide-arrow{position:absolute;top:267px;width:35px;height:35px;border-radius:50%;background:rgba(60,60,60,.55);display:flex;align-items:center;justify-content:center}
.slide-arrow.prev{left:54px}
.slide-arrow.next{left:1117px;background:rgba(60,60,60,.15)}
.login-panel{position:absolute;left:139px;top:162px;width:336px;height:354px;background:var(--panel-frame);padding:7px}
.login-card{width:100%;height:100%;background:#fbfbfb;position:relative}
.field{position:absolute;left:24px;width:273px;height:48px;border:1px solid var(--field-border);border-radius:3px;background:#fff;font-size:14px;color:var(--field-text);padding:0 19px;display:flex;align-items:center}
.field.email{top:26px}
.field.password{top:82px}
.forgot{position:absolute;left:26px;top:153px;display:flex;align-items:center;gap:10px;font-size:15px;color:#555}
.forgot .tick{width:16px;height:16px;border:1px solid #ccc;border-radius:50%;display:flex;align-items:center;justify-content:center}
.btn{position:absolute;top:194px;height:47px;width:129px;color:#fff;font-family:"Roboto",sans-serif;font-weight:500;font-size:17px;display:flex;align-items:center;justify-content:center;border-radius:2px}
.btn.signup{left:24px;background:var(--signup)}
.btn.login{left:167px;background:var(--login)}
.or{position:absolute;left:130px;top:233px;width:54px;height:54px;border-radius:50%;background:#fbfbfb;font-size:18px;color:#444;display:flex;align-items:center;justify-content:center;z-index:1}
.social-login{position:absolute;left:25px;top:273px;width:271px;height:48px;background:var(--social-login);border-radius:3px;display:flex;align-items:center;color:#fff;font-size:19px}
.social-login .mark{width:55px;height:100%;border-right:1px solid var(--social-login-dark);display:flex;align-items:center;justify-content:center}
.social-login .mark i{width:16px;height:16px;background:#fff;border-radius:2px}
.social-login span{padding-left:16px}
.site-footer{position:absolute;left:0;top:746px;width:1200px;height:159px;background:var(--footer-bg);text-align:center;color:var(--footer-text)}
.social{display:flex;justify-content:center;gap:13px;margin-top:33px}
.social span{width:25px;height:25px;background:var(--icon);border-radius:4px;display:flex;align-items:center;justify-content:center}
.copyright{font-size:13px;margin-top:14px}
.footer-links{font-size:14px;margin-top:13px;word-spacing:2px}
.footer-links a{color:var(--footer-text);text-decoration:none}
</style>
</head>
<body>
<header class="site-header">
  <div class="brand">Trondix<span class="brand-mark"></span></div>
  <nav class="main-nav"><a href="#">LOGIN</a><a href="#">HOW IT WORKS</a><a href="#">BUSINESS</a></nav>
  <div class="search"><span>SEARCH</span>
    <svg width="12" height="12" viewBox="0 0 12 12"><circle cx="5" cy="5" r="3.6" fill="none" stroke="#222" stroke-width="1.8"/><line x1="7.6" y1="7.6" x2="11" y2="11" stroke="#222" stroke-width="2"/></svg>
  </div>
  <div class="menu-btn"><i></i><i></i><i></i></div>
</header>

<section class="hero">
  <div class="hero-photo" role="img" aria-label="Smiling woman holding shopping bags and looking at her phone on a blurred city shopping street"></div>
  <div class="hero-title"><h1>SHOP DIRECTLY FROM YOUR PROFILE</h1><p>Save your time. Live better.</p></div>
  <div class="slide-arrow prev"><svg width="12" height="18" viewBox="0 0 12 18"><polyline points="10,1 2,9 10,17" fill="none" stroke="#fff" stroke-width="2"/></svg></div>
  <div class="slide-arrow next"><svg width="12" height="18" viewBox="0 0 12 18"><polyline points="2,1 10,9 2,17" fill="none" stroke="#fff" stroke-width="2"/></svg></div>

  <div class="login-panel">
    <div class="login-card">
      <div class="field email">E Mail</div>
      <div class="field password">Password</div>
      <div class="forgot"><span class="tick"><svg width="8" height="8" viewBox="0 0 8 8"><polyline points="1,4 3,6 7,1.5" fill="none" stroke="#333" stroke-width="1.5"/></svg></span>Forgot Password</div>
      <div class="btn signup">SIGN UP</div>
      <div class="btn login">LOGIN</div>
      <div class="or">OR</div>
      <div class="social-login"><div class="mark"><i></i></div><span>Login With Friendlane</span></div>
    </div>
  </div>
</section>

<footer class="site-footer">
  <div class="social">
    <span aria-label="Friendlane"></span>
    <span aria-label="Chirply"></span>
    <span aria-label="Workmesh"></span>
    <span aria-label="Glimmora"></span>
    <span aria-label="Phone"><svg width="15" height="15" viewBox="0 0 16 16"><path d="M3 1.5l3 0 1 3.5-2 1.5c1 2 2.5 3.5 4.5 4.5l1.5-2 3.5 1 0 3c0 .8-.7 1.5-1.5 1.5C7 14.5 1.5 9 1.5 3c0-.8.7-1.5 1.5-1.5z" fill="#1b1b1b"/></svg></span>
  </div>
  <p class="copyright">Copyright (c) 2015 Trondix. All rights reserved.</p>
  <p class="footer-links"><a href="#">About us</a> / <a href="#">Blog</a> / <a href="#">Business</a> / <a href="#">Jobs</a> / <a href="#">Privacy</a> / <a href="#">FAQ</a> / <a href="#">Contacts</a></p>
</footer>
</body>
</html>
```